candle postcard

We need a postcard telling customers about our new line of candles to go along with our bath and body product line. We like pretty and clean. dont love clip art.
Like the postcard to say something like:
If you love what Bloom, A Herbarium does for your body, wait until you see what we’ve got in store for your home. We’ve taken 4 popular Aroma Blends: Santorini, Chamomile Flower, Vanilla Plum and Lavender Mint, and transformed them into a range of luxury soy-based candles. Pair a candle with any of our nourishing skin care products to create the ultimate at-home spa experience or give them as the perfect, pampering gift.

For more info or to order:
info@bloomaherbarium-example.com
bloomaherbarium-example.com
800.471.3962

Return address:
418 Fenwick Ave
Dayton, OH 45492

```html
<!DOCTYPE html>
<html lang="en">
<head>
<meta charset="utf-8">
<title>Bloom, A Herbarium – Candle Postcard</title>
<link rel="stylesheet" href="https://fonts.googleapis.com/css2?family=Open+Sans:ital,wght@0,400;0,600;1,700&family=Roboto+Condensed:ital,wght@0,400;1,700&display=swap">
<style>
  :root {
    --stage: #2b2b2b;
    --paper: #ffffff;
    --ice: #e6f1fa;
    --sky: #b9d6f0;
    --sky-deep: #8fb8e2;
    --teal: #2f8a78;
    --mint: #6cc7b4;
    --ink: #1d1d1d;
    --body: #333333;
    --white: #ffffff;
  }
  * { margin: 0; padding: 0; box-sizing: border-box; }
  html, body { width: 1200px; height: 1144px; overflow: hidden; background: var(--stage); }
  .canvas { position: relative; width: 1200px; height: 1144px; }

  /* Back of card */
  .card-back {
    position: absolute; left: 40px; top: 20px; width: 693px; height: 545px;
    background: linear-gradient(180deg, var(--ice) 0%, var(--paper) 40%, var(--paper) 100%);
    overflow: hidden;
  }
  .card-back .swoosh { position: absolute; inset: 0; }
  .product-shot {
    position: absolute; left: 38px; top: 22px; width: 167px; height: 138px;
    background: linear-gradient(135deg, #f6e37a 0%, #d9b2e0 45%, #a9b8ea 75%, #f4f1dd 100%);
    border-radius: 2px;
  }
  .brand-name {
    position: absolute; left: 215px; top: 72px; width: 300px; text-align: center;
    font-family: "Open Sans", sans-serif; font-weight: 400; font-size: 28px;
    color: var(--mint); letter-spacing: 0.5px;
  }
  .return-address {
    position: absolute; left: 243px; top: 153px;
    font-family: "Roboto Condensed", sans-serif; font-size: 13.5px; color: var(--body);
  }
  .stamp-area {
    position: absolute; left: 531px; top: 31px; width: 134px; height: 130px;
    background: rgba(185, 214, 240, 0.5);
  }
  .pitch { position: absolute; left: 34px; top: 178px; width: 300px; }
  .pitch-title {
    font-family: "Open Sans", sans-serif; font-style: italic; font-weight: 700;
    font-size: 19px; line-height: 25px; color: var(--teal);
  }
  .pitch-copy {
    margin-top: 2px;
    font-family: "Open Sans", sans-serif; font-size: 13.5px; line-height: 18.6px; color: var(--body);
  }
  .order-info {
    margin-top: 10px;
    font-family: "Open Sans", sans-serif; font-style: italic; font-weight: 700;
    font-size: 13.5px; line-height: 19px; color: var(--ink);
  }

  /* Front of card */
  .card-front {
    position: absolute; left: 450px; top: 582px; width: 710px; height: 550px; overflow: hidden;
  }
  .hero-photo {
    position: absolute; inset: 0;
    background:
      radial-gradient(ellipse 60% 45% at 25% 85%, rgba(214, 96, 104, 0.9) 0%, rgba(214, 96, 104, 0) 70%),
      radial-gradient(ellipse 50% 55% at 35% 35%, #f0d2c2 0%, rgba(240, 210, 194, 0) 75%),
      radial-gradient(ellipse 40% 50% at 75% 25%, #f3dccf 0%, rgba(243, 220, 207, 0) 75%),
      linear-gradient(90deg, #7a4a33 0%, #c99a82 30%, #d9b3a0 55%, #3a2a26 80%, #151212 100%);
  }
  .brand-tab {
    position: absolute; left: 0; top: 48px; width: 276px; height: 102px;
    background: rgba(255, 255, 255, 0.82);
    border-radius: 0 40px 40px 0;
  }
  .brand-tab .brand-name {
    left: 0; top: 34px; width: 260px; font-size: 24px;
  }
  .headline {
    position: absolute; left: 390px; top: 286px; width: 300px; text-align: center;
    font-family: "Roboto Condensed", sans-serif; font-style: italic; font-weight: 700;
    font-size: 21px; line-height: 25px; color: var(--white);
  }
  .front-contact {
    position: absolute; left: 450px; top: 436px;
    font-family: "Roboto Condensed", sans-serif; font-style: italic; font-weight: 700;
    font-size: 13.5px; line-height: 19.5px; color: var(--white);
  }
</style>
</head>
<body>
<main class="canvas">

  <section class="card-back">
    <svg class="swoosh" width="693" height="545" viewBox="0 0 693 545" aria-hidden="true">
      <defs>
        <linearGradient id="wave" x1="0" y1="0" x2="1" y2="0">
          <stop offset="0" stop-color="#8fb8e2" stop-opacity="0.8"/>
          <stop offset="0.6" stop-color="#b9d6f0" stop-opacity="0.4"/>
          <stop offset="1" stop-color="#ffffff" stop-opacity="0"/>
        </linearGradient>
      </defs>
      <path d="M0 460 C120 380 260 350 420 330 C300 390 180 430 0 500 Z" fill="url(#wave)"/>
      <path d="M0 330 C150 360 260 350 400 330 C260 380 140 400 0 390 Z" fill="#b9d6f0" opacity="0.35"/>
      <path d="M500 0 C560 90 620 150 693 180 L693 230 C610 190 540 110 480 0 Z" fill="#b9d6f0" opacity="0.35"/>
      <path d="M0 545 L0 480 C140 440 280 420 420 410 C300 450 160 500 80 545 Z" fill="#e6f1fa"/>
    </svg>

    <div class="product-shot" role="img" aria-label="Photo of soy blend candle boxes in yellow, pink, purple and blue with a glass candle"></div>

    <div class="brand-name">Bloom, A Herbarium</div>
    <p class="return-address">Return address: 418 Fenwick Ave Dayton, OH 45492</p>
    <div class="stamp-area"></div>

    <div class="pitch">
      <h2 class="pitch-title">We’ve taken<br>4 popular Aroma Blends:</h2>
      <p class="pitch-copy">Santorini, Chamomile Flower, Vanilla Plum and Lavender Mint, and transformed them into a range of luxury soy-based candles. Pair a candle with any of our nourishing skin care products to create the ultimate at-home spa experience or give them as the perfect, pampering gift.</p>
      <p class="order-info">For more info or to order:<br>info@bloomaherbarium-example.com<br>bloomaherbarium-example.com<br>800.471.3962</p>
    </div>
  </section>

  <section class="card-front">
    <div class="hero-photo" role="img" aria-label="Photo of two smiling women cheek to cheek above lit pink pillar candles and white lilies"></div>
    <div class="brand-tab">
      <div class="brand-name">Bloom, A Herbarium</div>
    </div>
    <h1 class="headline">If you love what Bloom,<br>A Herbarium does for your body,<br>wait until you see what we’ve got<br>in store for your home.</h1>
    <p class="front-contact">Address: 418 Fenwick Ave Dayton, OH 45492<br>Phone: 800.471.3962<br>www.bloomaherbarium-example.com</p>
  </section>

</main>
</body>
</html>
```